Flyer-Design für Personalvermittlung
Zielgruppe
Wir machen Personalvermittlung (www.kraftwendel.de), Unternehmen, die einen eigenen Kunden haben sowie Unternehmen, die Kundenservice als Dienstleistung anbieten. DIe Zielgruppe sind Personalentscheider, Recruiter, HR-Direktoren, Kundenservicecenter-Leiter, Geschäftsführer). Weiterhin zählt zur Zielgruppe jeder wechselwillige Kandidat, der sich bei kraftwendel registrieren kann.
Aufgabenstellung
Ich hätte gerne ein zweiseitiges Flyerformat, was über Hostessen verteilbar ist, also nicht größer als A5. Inhalte können gerne aus der Homepage entnommen werden. Weiterhin in der Anlage ein Teaser, den wir Unternehmen zur Verfügung stellen. Vorderseite für Unternehmen, Rückseite für Kandidaten. Kernige Aussagen, wenig Text.

```html
<!DOCTYPE html>
<html lang="de">
<head>
<meta charset="utf-8">
<title>kraftwendel – Flyer Unternehmen</title>
<link href="https://fonts.googleapis.com/css2?family=Arimo:wght@400;700&display=swap" rel="stylesheet">
<style>
:root{
  --teal:#7dc6b2;
  --navy:#1e2330;
  --ink:#1e2330;
  --white:#ffffff;
  --muted:#d9dde3;
}
*{margin:0;padding:0;box-sizing:border-box}
html,body{width:846px;height:1200px;overflow:hidden;background:var(--white)}
body{font-family:"Arimo",Arial,sans-serif;color:var(--ink);position:relative}
.brand{position:absolute;left:339px;top:20px;display:flex;align-items:center}
.brand-dot{width:168px;height:168px;border-radius:50%;background:var(--navy)}
.brand-text{margin-left:14px}
.brand-name{font-size:29px;font-weight:700;line-height:1;color:var(--navy)}
.brand-tagline{font-size:12.5px;margin-top:4px;color:var(--navy)}
.hero-band{position:absolute;left:0;top:221px;width:846px;height:79px;background:var(--teal);
  color:var(--white);font-weight:700;font-size:26px;line-height:29px;text-align:center;padding-top:10px}
.audience-tab{position:absolute;left:814px;top:325px;width:32px;height:626px;background:var(--navy)}
.audience-tab span{position:absolute;left:7px;top:20px;writing-mode:vertical-rl;color:var(--white);
  font-size:15.5px;font-weight:700;letter-spacing:.5px}
.benefit{position:absolute;top:333px;width:240px;text-align:center}
.benefit-icon{width:95px;height:95px;border-radius:50%;background:var(--teal);margin:0 auto;display:flex;align-items:center;justify-content:center}
.benefit-title{font-size:15.5px;font-weight:700;margin-top:20px}
.benefit-text{font-size:16px;line-height:18.2px;margin-top:17px;white-space:nowrap}
.benefit-text b{font-weight:700}
.b1{left:66px}.b2{left:303px}.b3{left:538px}
.skyline{position:absolute;left:86px;top:767px;width:673px;height:131px;
  background:linear-gradient(90deg,#5a6e82 0%,#9aa8b5 30%,#e6eaee 50%,#b4c1cc 75%,#4d6f94 100%)}
.slogan-band{position:absolute;left:86px;top:912px;width:673px;height:38px;background:var(--teal);
  color:var(--white);font-size:26px;font-weight:700;text-align:center;line-height:38px}
.cta{position:absolute;left:0;top:994px;width:846px;text-align:center;font-size:28px;font-weight:700;line-height:29px;color:var(--navy)}
.footer{position:absolute;left:0;top:1071px;width:846px;height:129px;background:var(--navy);color:var(--muted)}
.contact{position:absolute;top:20px;width:160px;text-align:center;font-size:12.5px;line-height:15px}
.contact svg{display:block;margin:0 auto 8px}
.contact .text{min-height:45px;display:flex;flex-direction:column;justify-content:center}
.c1{left:-3px}.c2{left:170px}.c3{left:343px}.c4{left:516px}.c5{left:688px}
</style>
</head>
<body>
<header class="brand">
  <div class="brand-dot"></div>
  <div class="brand-text">
    <div class="brand-name">kraftwendel.de</div>
    <div class="brand-tagline">Das Karriereportal im Kundenservice</div>
  </div>
</header>

<div class="hero-band">Finden Sie die besten Mitarbeiter für Ihre Aufgaben<br>im Kundenservice und im Call Center!</div>

<div class="audience-tab"><span>UNTERNEHMEN</span></div>

<section class="benefit b1">
  <div class="benefit-icon">
    <svg width="70" height="70" viewBox="0 0 70 70" fill="none" stroke="#fff" stroke-width="3" stroke-linejoin="round">
      <circle cx="34" cy="14" r="6"/>
      <path d="M14 36c0-10 9-16 22-16s22 6 22 16c0 6-3 10-7 13v7h-7v-4H27v4h-7v-7c-3-2-5-4-6-7H9v-9h5z"/>
      <path d="M28 30h12"/><circle cx="20" cy="34" r="1" fill="#fff"/><path d="M58 34c3 0 5-2 5-4"/>
    </svg>
  </div>
  <div class="benefit-title">GÜNSTIGER</div>
  <p class="benefit-text"><b>kraftwendel</b> ist bis zu 50<br>Prozent günstiger als die<br>klassischen Headhunter<br>und Vermittlungsagenturen.<br>Die ersten 50% unseres<br>Erfolgshonorars zahlen Sie<br>bei Unterzeichnung des<br>jeweiligen Arbeitsvertrages.<br>Die anderen 50% zahlen<br>Sie nur, wenn der Kandidat<br>die Probezeit erfolgreich<br>bestanden hat.</p>
</section>

<section class="benefit b2">
  <div class="benefit-icon">
    <svg width="44" height="50" viewBox="0 0 44 50">
      <path d="M22 2 41 9v14c0 12-8 21-19 25C11 44 3 35 3 23V9z" fill="#fff"/>
      <path d="M13 25l7 7 12-13" fill="none" stroke="var(--teal)" stroke-width="4" stroke-linecap="round" stroke-linejoin="round"/>
    </svg>
  </div>
  <div class="benefit-title">RISIKOLOS</div>
  <p class="benefit-text"><b>kraftwendel</b> bietet Ihnen<br>ein erfolgsbasiertes<br>Honorarmodell. Sie zahlen<br>nur bei einer erfolgreichen<br>Personalvermittlung.<br>Sie zahlen nichts im Voraus<br>für den Beginn unserer<br>Suche. Somit ist bis zur<br>Unterzeichnung eines<br>Arbeitsvertrages unser<br>Service für Sie kostenfrei.</p>
</section>

<section class="benefit b3">
  <div class="benefit-icon">
    <svg width="64" height="64" viewBox="0 0 64 64" fill="none" stroke="#fff" stroke-width="3" stroke-linejoin="round">
      <path d="M8 34 22 20a6 6 0 1 1 8-8l8-8 8 8a6 6 0 1 0 8 8l4 4-14 14a6 6 0 1 1-8 8l-8 8-8-8a6 6 0 1 0-8-8z"/>
    </svg>
  </div>
  <div class="benefit-title">PASSEND</div>
  <p class="benefit-text">Durch unseren Pairing-<br>Algorithmus erhalten Sie<br>von uns ausschließlich<br>passende Kandidaten<br>angeboten.<br>Sie haben spezielle<br>Wünsche an den<br>Kandidaten? Auch das ist<br>kein Problem. Wir matchen<br>passgenau. Im Zweifel<br>suchen wir für Sie gezielt<br>und diskret durch<br>persönliche und direkte<br>Kandidatenansprache.</p>
</section>

<div class="skyline" role="img" aria-label="Foto einer modernen Bürofassade vor einer Hochhaus-Skyline"></div>

<div class="slogan-band">Suchen. Finden. Starten.</div>

<h2 class="cta">Worauf warten Sie noch?<br>Jetzt anmelden und neuen Job finden!</h2>

<footer class="footer">
  <div class="contact c1">
    <svg width="24" height="28" viewBox="0 0 24 28" fill="none" stroke="#d9dde3" stroke-width="1.6"><path d="M12 27S2 16 2 11a10 10 0 0 1 20 0c0 5-10 16-10 16z"/><circle cx="12" cy="11" r="4"/></svg>
    <div class="text">kraftwendel GmbH<br>Lindenhofweg 42<br>10435 Berlin</div>
  </div>
  <div class="contact c2">
    <svg width="28" height="28" viewBox="0 0 28 28" fill="none" stroke="#d9dde3" stroke-width="1.6" stroke-linejoin="round"><path d="M2 14 14 3l12 11M6 11v14h6v-7h4v7h6V11"/></svg>
    <div class="text">www.kraftwendel.de</div>
  </div>
  <div class="contact c3">
    <svg width="28" height="28" viewBox="0 0 28 28" fill="none" stroke="#d9dde3" stroke-width="1.6"><circle cx="14" cy="14" r="12.5"/><path d="M9 8l3 0 1 4-2 1c1 2 2 3 4 4l1-2 4 1v3c-6 1-12-5-11-11z" fill="#d9dde3"/></svg>
    <div class="text">49 [0]30 555 013 270</div>
  </div>
  <div class="contact c4">
    <svg width="28" height="28" viewBox="0 0 28 28" fill="none" stroke="#d9dde3" stroke-width="1.6"><circle cx="14" cy="14" r="12.5"/></svg>
    <div class="text">kraftwendel_DE</div>
  </div>
  <div class="contact c5">
    <svg width="30" height="28" viewBox="0 0 30 28" fill="none" stroke="#d9dde3" stroke-width="1.6"><rect x="2" y="5" width="26" height="18"/><path d="M2 5l13 11L28 5M2 23l10-9M28 23l-10-9"/></svg>
    <div class="text">info@kraftwendel.de</div>
  </div>
</footer>
</body>
</html>
```